11 x 17 Thelanoros Quote

Design the following quote in a poster.

"First say to yourself what you would be; then do what you have to do." - Thelanoros

See here for inspiration - https://prints.quietgrove.com/

Quote

```html
<!DOCTYPE html>
<html lang="en">
<head>
<meta charset="utf-8">
<title>Thelanoros Quote Poster</title>
<link href="https://fonts.googleapis.com/css2?family=Passion+One:wght@700&family=Kaushan+Script&display=swap" rel="stylesheet">
<style>
  :root {
    --backdrop: #e6e6e6;
    --paper: #ffffff;
    --ink: #1d1a16;
    --ink-shadow: #bdbdbd;
  }
  * { margin: 0; padding: 0; box-sizing: border-box; }
  html, body {
    width: 1200px;
    height: 1200px;
    overflow: hidden;
    background: var(--backdrop);
  }
  .poster {
    position: absolute;
    left: 197px;
    top: 30px;
    width: 806px;
    height: 1140px;
    background: var(--paper);
  }
  .quote {
    font-family: "Passion One", "Arial Black", sans-serif;
    font-weight: 700;
    text-transform: uppercase;
    color: var(--ink);
    text-shadow: 3px 3px 0 var(--ink-shadow);
    line-height: 1;
  }
  .quote-line {
    position: absolute;
    white-space: nowrap;
    display: flex;
    align-items: baseline;
    gap: 12px;
  }
  .line-one   { left: 36px; top: 326px; font-size: 48px; }
  .line-two   { left: 60px; top: 400px; font-size: 48px; }
  .line-three { left: 93px; top: 528px; font-size: 48px; }
  .line-four  { left: 66px; top: 654px; font-size: 120px; letter-spacing: 1px; }
  .emphasis   { font-size: 132px; }
  .open-mark  { font-size: 100px; line-height: 0.5; align-self: flex-start; margin-top: 8px; margin-right: -6px; }
  .close-mark { font-size: 110px; margin-left: -14px; }
  .attribution {
    position: absolute;
    left: 185px;
    top: 888px;
    font-family: "Kaushan Script", cursive;
    font-size: 66px;
    color: var(--ink);
  }
</style>
</head>
<body>
  <main class="poster">
    <blockquote class="quote">
      <div class="quote-line line-one"><span class="open-mark">“</span><span>First say to yourself</span></div>
      <div class="quote-line line-two"><span>what</span><span class="emphasis">You</span><span>would be;</span></div>
      <div class="quote-line line-three"><span>then do what</span><span class="emphasis">You</span></div>
      <div class="quote-line line-four"><span>Have to do.</span><span class="close-mark">”</span></div>
    </blockquote>
    <p class="attribution">– Thelanoros</p>
  </main>
</body>
</html>
```